Orvella Aid Fund - New Website Design

I need a site that looks like this http://renwick-gives-now.org for boat donations. So please replace the cars with boats.

```html
<!DOCTYPE html>
<html lang="en">
<head>
<meta charset="utf-8">
<title>Orvella Aid Fund – Donate Boats to Charity</title>
<link href="https://fonts.googleapis.com/css2?family=Bitter:wght@400;500&family=Lato:wght@400;700&display=swap" rel="stylesheet">
<style>
:root{
  --teal:#2a8d91;
  --teal-dark:#1f7175;
  --teal-panel:rgba(36,120,124,.93);
  --ink:#333;
  --ink-soft:#444;
  --sky:#c9ecf1;
  --white:#fff;
  --rule:#cfd8da;
  --pink-a:#e7a3a6;
  --pink-b:#c9787d;
}
*{box-sizing:border-box;margin:0;padding:0}
html,body{width:818px;height:1200px;overflow:hidden;background:var(--white)}
body{position:relative;font-family:"Lato",Arial,sans-serif;color:var(--ink)}
.abs{position:absolute}

.top-rule{left:0;top:0;width:818px;height:3px;background:var(--teal)}
.brand{left:55px;top:26px;display:flex;align-items:center;gap:10px}
.brand-mark{width:34px;height:34px;background:var(--teal)}
.brand-name{font-family:"Lato",sans-serif;font-size:19px;color:var(--ink-soft);line-height:1.05;width:110px}
.call{left:424px;top:30px;display:flex;align-items:center;gap:8px;font-family:"Lato",sans-serif;font-size:17px;color:var(--ink-soft);white-space:nowrap}
.call-icon{width:26px;height:26px;border-radius:50%;background:var(--teal-dark);display:flex;align-items:center;justify-content:center;flex:none}
.btn-donate{left:644px;top:29px;width:121px;height:28px;background:var(--teal);color:var(--white);font-size:13px;display:flex;align-items:center;justify-content:center;gap:10px}

.nav{left:0;top:92px;width:818px;height:33px;background:var(--teal)}
.nav a{position:absolute;top:0;height:33px;line-height:33px;color:var(--white);font-family:"Bitter",serif;font-weight:500;font-size:11px;text-decoration:none;letter-spacing:.2px}
.nav a.active{background:var(--teal-dark);width:87px;text-align:center}
.nav .sep{position:absolute;top:10px;width:1px;height:13px;background:rgba(255,255,255,.35)}

.hero{left:0;top:125px;width:818px;height:364px;background:linear-gradient(90deg,#d9cdd0 0%,var(--pink-a) 35%,var(--pink-b) 100%)}
.hero-photo{left:0;top:0;width:340px;height:364px;background:linear-gradient(160deg,#f2c6d9 0%,#e9dcd6 45%,#d7d6d8 100%)}
.hero-title{right:310px;top:140px;text-align:right;font-family:"Bitter",serif;font-size:31px;line-height:31px;color:var(--teal-dark);white-space:nowrap}
.hero-sub{right:310px;top:207px;font-family:"Bitter",serif;font-size:14px;color:#3a3a3a;white-space:nowrap}

.form-tab-l{left:497px;top:80px;width:0;height:0;border-bottom:10px solid var(--teal-dark);border-left:10px solid transparent}
.form-tab-r{left:765px;top:80px;width:0;height:0;border-bottom:10px solid var(--teal-dark);border-right:10px solid transparent}
.form{left:507px;top:80px;width:258px;height:343px;background:var(--teal-panel);border-radius:0 0 5px 5px;color:var(--white)}
.form h2{position:absolute;left:0;top:13px;width:100%;text-align:center;font-family:"Bitter",serif;font-weight:400;font-size:20px}
.form .line{position:absolute;left:0;top:44px;width:100%;height:1px;background:rgba(255,255,255,.25)}
.form h3{position:absolute;left:12px;font-weight:400;font-size:12.5px}
.field{position:absolute;height:24px;background:var(--white);color:#888;font-size:7.5px;padding-left:7px;line-height:24px}
.field.select{color:#333;height:25px;line-height:25px;border:1px solid #bbb}
.field.select i{position:absolute;right:1px;top:1px;width:9px;height:21px;background:#e6e6e6;border:1px solid #999}
.field.select i::after{content:"";position:absolute;left:2px;top:8px;border-left:2px solid transparent;border-right:2px solid transparent;border-top:3px solid #111}
.btn-submit{position:absolute;left:73px;top:286px;width:111px;height:27px;background:var(--teal);color:var(--white);font-size:11px;display:flex;align-items:center;justify-content:center}

.welcome{left:0;top:489px;width:818px;height:230px;background:var(--sky)}
.sec-title{width:818px;left:0;text-align:center;font-family:"Bitter",serif;font-size:30px;color:#2f2f2f;letter-spacing:.5px}
.sec-title span{color:var(--teal-dark)}
.divider{left:161px;width:496px;height:1px;background:var(--rule)}
.divider b{position:absolute;left:234px;top:-5px;width:28px;height:10px;background:var(--sky)}
.divider b::after{content:"";position:absolute;left:9px;top:0;width:10px;height:10px;border-radius:50%;background:#e0a848}
.welcome-text{left:0;width:818px;text-align:center;font-size:9px;color:#333}
.welcome-text strong{font-weight:700}
.btn-read{left:371px;top:172px;width:77px;height:23px;background:var(--teal);color:var(--white);font-size:11px;display:flex;align-items:center;justify-content:center}

.sec-sub{left:0;width:818px;text-align:center;font-size:14px;color:#333;font-weight:400}
.hub{left:0;top:0;width:818px;height:1200px}
.feature{font-size:11px;line-height:14px;color:#333}
.feature.l{text-align:right}
.hub-name{left:330px;top:967px;width:160px;text-align:center;font-size:16px;color:var(--teal-dark)}
</style>
</head>
<body>
<div class="abs top-rule"></div>

<header>
  <div class="abs brand">
    <div class="brand-mark"></div>
    <div class="brand-name">Orvella Aid Fund</div>
  </div>
  <div class="abs call">
    <span class="call-icon">
      <svg width="14" height="14" viewBox="0 0 24 24"><path fill="#fff" d="M6.6 10.8a15.1 15.1 0 0 0 6.6 6.6l2.2-2.2c.3-.3.7-.4 1-.2 1.1.4 2.3.6 3.6.6.6 0 1 .4 1 1V20c0 .6-.4 1-1 1A17 17 0 0 1 3 4c0-.6.4-1 1-1h3.5c.6 0 1 .4 1 1 0 1.3.2 2.5.6 3.6.1.3 0 .7-.2 1l-2.3 2.2z"/></svg>
    </span>
    <span>Call : 1-800-555-0148</span>
  </div>
  <div class="abs btn-donate">Donate Now
    <svg width="14" height="14" viewBox="0 0 24 24"><circle cx="10" cy="8" r="5" fill="none" stroke="#fff" stroke-width="2"/><path d="M3 21c1-4 4-6 7-6s4 1 5 2" fill="none" stroke="#fff" stroke-width="2"/><path d="M15 17h6" stroke="#fff" stroke-width="2"/></svg>
  </div>
</header>

<nav class="abs nav">
  <a class="active" href="#" style="left:55px">HOME</a>
  <a href="#" style="left:170px">ABOUT US</a>
  <span class="sep" style="left:252px"></span>
  <a href="#" style="left:280px">GET STARTED</a>
  <span class="sep" style="left:378px"></span>
  <a href="#" style="left:406px">CONTACT US</a>
</nav>

<section class="abs hero">
  <div class="abs hero-photo" role="img" aria-label="Photo of a smiling young girl wearing a pink patterned headscarf and a light jacket"></div>
  <h1 class="abs hero-title" style="font-weight:400">Donate boats to<br>Charity!</h1>
  <p class="abs hero-sub">Your boats can make a difference</p>
</section>

<div class="abs form-tab-l"></div>
<div class="abs form-tab-r"></div>
<form class="abs form">
  <h2>Donation Pick Up Form</h2>
  <div class="line"></div>
  <h3 style="top:57px">Contact Information</h3>
  <div class="field" style="left:12px;top:82px;width:110px">First Name</div>
  <div class="field" style="left:135px;top:82px;width:110px">Last Name</div>
  <div class="field" style="left:12px;top:115px;width:110px">Zip Code</div>
  <div class="field" style="left:135px;top:115px;width:110px">Day Phone</div>
  <div class="field" style="left:12px;top:148px;width:233px">Email Address</div>
  <h3 style="top:181px">Auto Donation Information</h3>
  <div class="field select" style="left:12px;top:209px;width:110px">Choose Year<i></i></div>
  <div class="field select" style="left:135px;top:209px;width:110px">Choose Make<i></i></div>
  <div class="field" style="left:12px;top:246px;width:233px">Model of Boat</div>
  <div class="btn-submit">Submit Application</div>
</form>

<section class="abs welcome">
  <h2 class="abs sec-title" style="top:30px;font-weight:400">WELCOME TO <span>OAF</span></h2>
  <div class="abs divider" style="top:92px"><b></b></div>
  <p class="abs welcome-text" style="top:117px"><strong>Orvella Aid Fund's</strong> mission is to improve, empower and to bring joy to the lives of children and their families affected by cancer.</p>
  <p class="abs welcome-text" style="top:144px"><strong style="color:var(--teal-dark)">OAF</strong> adapts its support to fit each child's needs; from education to assistance with treatment, recovery and family support.</p>
  <div class="abs btn-read">Read More</div>
</section>

<section>
  <h2 class="abs sec-title" style="top:752px;font-weight:400">DONATE BOATS TO <span>CHARITY!</span></h2>
  <p class="abs sec-sub" style="top:790px">Your boats can make a difference!</p>
  <div class="abs divider" style="top:832px"><b style="background:#fff"></b></div>

  <svg class="abs hub" viewBox="0 0 818 1200" width="818" height="1200">
    <defs>
      <g id="node">
        <circle r="30" fill="#fff" stroke="#e3eeef" stroke-width="3"/>
        <circle r="25" fill="#2a8d91"/>
      </g>
    </defs>
    <circle cx="410" cy="985" r="95" fill="#fff" stroke="#777" stroke-width="1.3" stroke-dasharray="1.5 2.5"/>
    <g stroke="#2a8d91" stroke-width="1.2">
      <line x1="306" y1="900" x2="341" y2="919"/>
      <line x1="282" y1="983" x2="315" y2="983"/>
      <line x1="306" y1="1066" x2="340" y2="1048"/>
      <line x1="513" y1="900" x2="479" y2="919"/>
      <line x1="536" y1="983" x2="504" y2="983"/>
      <line x1="513" y1="1066" x2="480" y2="1048"/>
    </g>
    <g fill="#fff" stroke="#2a8d91" stroke-width="2">
      <circle cx="341" cy="919" r="4.5"/><circle cx="315" cy="983" r="4.5"/><circle cx="340" cy="1048" r="4.5"/>
      <circle cx="479" cy="919" r="4.5"/><circle cx="504" cy="983" r="4.5"/><circle cx="480" cy="1048" r="4.5"/>
    </g>
    <use href="#node" x="286" y="884"/><use href="#node" x="252" y="983"/><use href="#node" x="286" y="1083"/>
    <use href="#node" x="533" y="884"/><use href="#node" x="566" y="983"/><use href="#node" x="533" y="1083"/>

    <g fill="#fff">
      <path d="M271 886h30l-5 7h-21z"/><path d="M279 880h12l4 5h-18z"/>
      <path d="M237 985h30l-5 6h-22z"/><path d="M245 977h10l5 7h-17z"/><rect x="251" y="972" width="2" height="6"/>
      <rect x="276" y="1074" width="14" height="6" rx="1" transform="rotate(-40 283 1077)"/>
      <rect x="281" y="1080" width="3" height="14" transform="rotate(-40 282 1087)"/>
      <rect x="284" y="1092" width="14" height="3"/>
    </g>
    <g fill="none" stroke="#fff" stroke-width="2">
      <path d="M533 897c-9-7-15-11-15-17a7 7 0 0 1 15-3 7 7 0 0 1 15 3c0 6-6 10-15 17z"/>
      <circle cx="533" cy="1083" r="11"/>
      <path d="M537 1077c-2-2-8-2-8 2s8 2 8 6-6 4-8 2M533 1073v20"/>
    </g>
    <g fill="#fff">
      <rect x="560" y="980" width="14" height="11"/><rect x="558" y="976" width="18" height="4"/>
      <rect x="552" y="986" width="5" height="9"/>
    </g>
  </svg>

  <div class="abs hub-name">Orvella Aid Fund</div>

  <p class="abs feature l" style="left:150px;top:871px;width:95px">Free Towing In<br>24-48 Hours</p>
  <p class="abs feature l" style="left:120px;top:971px;width:90px">We Accept<br>All boats</p>
  <p class="abs feature l" style="left:90px;top:1071px;width:155px">boats Will Be Sold on the<br>Largest Auction Network</p>
  <p class="abs feature" style="left:575px;top:871px;width:150px">boats Donations Help Fund<br>Charitable Programs</p>
  <p class="abs feature" style="left:609px;top:971px;width:100px">Hassle<br>Free Donation</p>
  <p class="abs feature" style="left:575px;top:1071px;width:100px">Income<br>Tax Deduction</p>
</section>
</body>
</html>
```